Corvane Energy Residential Solar System Sale Letterbox Flyer

We require a professional looking letterbox flyer to advertise our current sales on installed residential solar systems. We are an expert in the field. With fully accredited VMA design and installation teams. We only use quality products and all work is completed in house and never subcontracted out meaning a high level of quality control is achieved. We require the flyer to be eye catching promoting the financial benefits of installing solar and the low capital outlay required. It should be enticing and have a push element to get people to take up the offer. The final design should allow us to keep the major design work but be able to change the price and size of the solar system depending on market fluctuations.

Target Market(s)

Homeowners

Font styles to use
Serif

Requirements
Must have
• Generic picture of solar panels. Picture of of Tarvo inverter. Ideally picture of panels + inverter for each system package size to visually display that they are packages. Must include our company logo.
• Must convey a v very professional and reliable feel to the client.
Nice to have
• 2 pages with system sales on the front etc. Company info on the back maybe. Picture of house with solar panels or panels being installed on a house.
• Wording that is provided can be incorporated however best suits the design and some wording can converted into logo's or imagery if that best suits the design also.
Should not have
• Pictures that are not pertinent to the Australian environment e.g.. a house in the snow. Should not look cheap.

```html
<!DOCTYPE html>
<html lang="en">
<head>
<meta charset="utf-8">
<title>Corvane Energy – Solar System Sale Flyer</title>
<link rel="stylesheet" href="https://fonts.googleapis.com/css2?family=Tinos:ital,wght@0,400;0,700;1,400&display=swap">
<style>
  :root {
    --navy: #2c3445;
    --red: #be1e2d;
    --ink: #2f3340;
    --sky-top: #ffffff;
    --sky-mid: #c9d8e4;
    --sky-low: #7fa6c4;
    --panel-dark: #1d3557;
    --panel-mid: #3d5f87;
    --panel-light: #8fb0cc;
  }
  * { box-sizing: border-box; margin: 0; padding: 0; }
  html, body { width: 848px; height: 1200px; overflow: hidden; background: #ffffff; }
  .flyer {
    position: relative;
    width: 848px;
    height: 1200px;
    overflow: hidden;
    font-family: "Tinos", "Times New Roman", serif;
    color: var(--ink);
    background: linear-gradient(180deg, var(--sky-top) 0%, var(--sky-top) 12%, var(--sky-mid) 42%, var(--sky-low) 72%, var(--sky-low) 100%);
  }
  .corner-bands { position: absolute; top: 0; left: 0; width: 848px; height: 1200px; }
  .brand-name {
    position: absolute;
    left: 24px; top: 46px;
    font-weight: 700;
    font-size: 24px;
    line-height: 1;
    color: var(--navy);
    white-space: nowrap;
  }
  .offers { position: absolute; left: 0; top: 0; width: 848px; text-align: center; }
  .offer-line { position: absolute; left: 0; width: 848px; line-height: 1; }
  .small { font-size: 17px; }
  .price { font-size: 22px; font-weight: 700; }
  .large { font-size: 25.5px; }
  .price-large { font-size: 31px; font-weight: 700; }
  .save-large { font-size: 23px; }
  .terms { position: absolute; left: 0; width: 848px; text-align: center; font-style: italic; font-size: 14.5px; line-height: 19.4px; white-space: nowrap; }
  .cta { position: absolute; left: 0; top: 780px; width: 848px; text-align: center; font-weight: 700; font-size: 26px; line-height: 32px; color: var(--ink); }
  .float-square { position: absolute; background: rgba(255,255,255,0.55); }
  .panel-photo {
    position: absolute; left: 0; top: 848px; width: 848px; height: 352px;
    background: linear-gradient(180deg, var(--panel-light) 0%, var(--panel-mid) 30%, var(--panel-dark) 100%);
  }
</style>
</head>
<body>
<main class="flyer">
  <svg class="corner-bands" viewBox="0 0 848 1200" aria-hidden="true">
    <polygon points="512,0 637,0 848,307 848,472" fill="var(--red)"/>
    <polygon points="652,0 848,0 848,285" fill="var(--navy)"/>
  </svg>

  <div class="float-square" style="left:404px;top:382px;width:42px;height:38px"></div>
  <div class="float-square" style="left:732px;top:445px;width:66px;height:66px"></div>
  <div class="float-square" style="left:781px;top:527px;width:42px;height:40px"></div>
  <div class="float-square" style="left:712px;top:543px;width:28px;height:28px"></div>
  <div class="float-square" style="left:757px;top:586px;width:17px;height:17px"></div>
  <div class="float-square" style="left:28px;top:756px;width:46px;height:44px"></div>
  <div class="float-square" style="left:120px;top:780px;width:18px;height:18px"></div>
  <div class="float-square" style="left:74px;top:806px;width:42px;height:42px"></div>
  <div class="float-square" style="left:15px;top:816px;width:22px;height:22px"></div>

  <header class="brand-name">Corvane Energy</header>

  <section class="offers">
    <p class="offer-line small" style="top:139px">6.5kW System 24 Tier 1 panels</p>
    <p class="offer-line small" style="top:161px">5kw Award winning Inverter</p>
    <p class="offer-line price" style="top:184px">Price from $2999</p>
    <p class="offer-line small" style="top:216px">Save up to $2000 per year on your electricity bills</p>

    <p class="offer-line small" style="top:291px">13kW System 48 Tier 1 Panels and 2 x 5kW inverters.</p>
    <p class="offer-line price" style="top:313px">Price from $5800</p>
    <p class="offer-line small" style="top:343px">Save up to $4000 per year on your electricity bills</p>

    <p class="offer-line large" style="top:451px">40kW System 148 Tier 1 Panels and 30kW Three Phase inverter.</p>
    <p class="offer-line price-large" style="top:479px">Price from $18,000</p>
    <p class="offer-line save-large" style="top:513px">Save up to $12000 per year on your electricity bills</p>
  </section>

  <p class="terms" style="top:567px">Prices include installation, GST and Government Rebate.</p>
  <p class="terms" style="top:605px">10 year warranty on panels and workmanship.<br>25 Year Performance warranty on panels.<br>5 year warranty on Inverters.&nbsp; (it is not necessary to have this written it could be in the<br>form of a 10 year warranty logo etc)</p>
  <p class="terms" style="top:699px">All systems are fully installed by our VMA accredited Design and Installation teams, to the<br>highest possible standards.</p>

  <p class="cta">Call us today on<br>0740 528 316</p>

  <div class="panel-photo" role="img" aria-label="Photograph of rows of blue solar panels under a clear sky"></div>
</main>
</body>
</html>
```